April 11th Event- Islamorada- Coaching/Tarot/Hypnotherapy

Hi! Need a flyer that can also be posted on social media. Directions attached. Also will need a version that 2 can fit on 1 piece of paper so I can cut in half for hand outs. PDF example attached as well so you can understand. Thank you!

AAAAAAAAAAAAAAAAAAAAAAAAAAAAAAAAAAAAAAAAAAAAAAAAAAAAAAAAAAAAAAAAAAAAAAAAAAAAAAAAAAAAAAAAAAAAAAAAAAAAAAAAAAAAAAAAAAAAAAAAAAAAAAAAAAAAAAAAAAAAAAAAAAAAAAAAAAAAAAAAAAAAAAAAAAAAAAAAAAAAAAAAAAAAAAAAAAAAAAAAAAAAAAAAAAAAAAAAAAAAAAAAAA

Target Market(s)

Female audience age 35-70.
Spiritual, sophisticated

Industry/Entity Type

Event Planning

Font styles to use
Serif

Colors
d2a4cc
3176b5
85acd3
b868aa
e667a6
eea4c8
f59296
fbf289
add136

Requirements
Must have
• See attachments
Nice to have
• See attachments

```html
<!DOCTYPE html>
<html lang="en">
<head>
<meta charset="utf-8">
<title>Open Yourself Up – Evening of Self Discovery</title>
<link href="https://fonts.googleapis.com/css2?family=Alegreya:ital,wght@0,400;0,500;0,700;1,700&family=Alegreya+Sans:ital,wght@0,400;0,500;1,400&family=Open+Sans:wght@700&display=swap" rel="stylesheet">
<style>
  :root{
    --teal:#6fa595;
    --teal-dark:#5e9586;
    --purple:#b064a6;
    --salmon:#f08a8e;
    --band:#72aa9a;
    --white:#ffffff;
    --bg-top:#dcefeb;
    --bg-mid:#eef3ea;
    --bg-low:#f3efef;
  }
  *{margin:0;padding:0;box-sizing:border-box}
  html,body{width:929px;height:1200px;overflow:hidden}
  body{background:#fff}
  .flyer{
    position:relative;width:929px;height:1200px;overflow:hidden;
    background:
      linear-gradient(rgba(255,255,255,.45) 1px,transparent 1px) 0 0/37px 19px,
      linear-gradient(90deg,rgba(255,255,255,.45) 1px,transparent 1px) 0 0/37px 19px,
      linear-gradient(180deg,var(--bg-top) 0%,#e6f2ee 35%,var(--bg-mid) 55%,var(--bg-low) 80%,#f6f2f3 100%);
  }
  .illustration{position:absolute;left:470px;top:0;width:459px;height:1200px;z-index:2}
  .t{position:absolute;left:45px;line-height:1;white-space:nowrap}
  .serif{font-family:"Alegreya",Georgia,serif}
  .sans{font-family:"Alegreya Sans","Trebuchet MS",sans-serif}
  .kicker{top:66px;font-size:29px;color:var(--purple)}
  .headline{top:110px;font-size:57px;font-weight:500;color:var(--teal);line-height:65px;
    text-shadow:1px 1px 0 var(--purple)}
  .intro{top:324px;font-size:19.5px;font-style:italic;color:var(--purple);line-height:28px;letter-spacing:.3px}
  .label{top:412px;font-size:19px;color:var(--teal)}
  .speaker-name{font-size:25px;color:var(--purple)}
  .rule{position:absolute;left:46px;height:2px;background:var(--teal)}
  .role{font-size:15.5px;color:var(--purple);letter-spacing:.3px}
  .role-sub{font-size:15.5px;color:var(--salmon);letter-spacing:.3px}
  .date{top:758px;font-size:37px;font-weight:500;color:var(--teal);text-shadow:1px 1px 0 var(--purple)}
  .day{top:810px;font-size:30px;color:var(--salmon);letter-spacing:.5px}
  .time{left:259px;top:760px;font-size:46px;font-weight:500;color:var(--teal);text-shadow:1px 1px 0 var(--purple)}
  .doors{left:259px;top:817px;font-size:19px;color:var(--salmon)}
  .venue{top:869px;font-size:28px;font-weight:500;color:var(--purple)}
  .address{top:908px;font-size:16px;color:var(--purple);letter-spacing:.3px}
  .address-sub{top:931px;font-size:15.5px;color:var(--salmon);letter-spacing:.3px}
  .tickets{top:974px;font-size:21px;color:var(--teal)}
  .tickets .sep{margin:0 6px}
  .guest{top:1003px;font-size:18px;color:var(--salmon);letter-spacing:.3px}
  .signoff{left:101px;top:1050px;font-size:24px;font-weight:700;font-style:italic;color:var(--purple)}
  .contact-band{position:absolute;left:0;top:1100px;width:929px;height:100px;background:var(--band);z-index:1}
  .contact{position:absolute;left:44px;font-family:"Open Sans",Arial,sans-serif;color:var(--white);z-index:3;white-space:nowrap}
  .contact-title{top:1124px;font-size:15px;font-weight:700}
  .contact-line{top:1154px;font-size:15.5px;font-weight:700}
  .contact-line .sep{margin:0 10px}
</style>
</head>
<body>
<div class="flyer">

  <svg class="illustration" viewBox="0 0 459 1200" role="img" aria-label="Hand-drawn illustration of a serene woman with closed eyes, her flowing hair rising into coral flames and birds, wearing a teal dress">
    <defs>
      <linearGradient id="illoTone" x1="0" y1="0" x2="0" y2="1">
        <stop offset="0" stop-color="#e98a7e" stop-opacity=".55"/>
        <stop offset=".35" stop-color="#e7b7a6" stop-opacity=".55"/>
        <stop offset=".6" stop-color="#efe6d2" stop-opacity=".7"/>
        <stop offset=".85" stop-color="#8fc4bb" stop-opacity=".8"/>
        <stop offset="1" stop-color="#7ab8ad" stop-opacity=".9"/>
      </linearGradient>
      <linearGradient id="illoFade" x1="0" y1="0" x2="1" y2="0">
        <stop offset="0" stop-color="#fff" stop-opacity="0"/>
        <stop offset=".25" stop-color="#fff" stop-opacity="1"/>
      </linearGradient>
      <mask id="illoMask"><rect width="459" height="1200" fill="url(#illoFade)"/></mask>
    </defs>
    <rect width="459" height="1200" fill="url(#illoTone)" mask="url(#illoMask)"/>
  </svg>

  <p class="t serif kicker">Get the 411:</p>
  <h1 class="t serif headline">Open Yourself Up<br>To The Info You<br>Have Inside</h1>
  <p class="t sans intro">PLEASE JOIN US FOR AN EVENING OF SELF<br>DISCOVERY, AND ENLIGHTMENT AND FUN!</p>

  <p class="t sans label">SPEAKERS:</p>

  <section class="speaker">
    <h2 class="t serif speaker-name" style="top:447px">Marisol Vance</h2>
    <span class="rule" style="top:480px;width:104px"></span>
    <p class="t sans role" style="top:492px">THE BRIGHT PATH LIFE COACH</p>
    <p class="t sans role-sub" style="top:512px">(CERTIFIED PROFESSIONAL LIFE COACH)</p>
  </section>

  <section class="speaker">
    <h2 class="t serif speaker-name" style="top:558px">Celeste Harlow</h2>
    <span class="rule" style="top:591px;width:104px"></span>
    <p class="t sans role" style="top:603px">LICENSED HYPNOTHERAPIST</p>
    <p class="t sans role-sub" style="top:623px">(SERENE HARBOR HOLISTIC THERAPIES)</p>
  </section>

  <section class="speaker">
    <h2 class="t serif speaker-name" style="top:670px">Joanna Sable</h2>
    <span class="rule" style="top:703px;width:104px"></span>
    <p class="t sans role" style="top:715px">TAROT READINGS/ EM PATH SPIRITUAL COUNSELOR</p>
  </section>

  <p class="t serif date">April 11th</p>
  <p class="t sans day">THURSDAY</p>
  <span class="rule" style="top:850px;width:104px"></span>
  <p class="t serif time">6PM–8PM</p>
  <p class="t sans doors">DOORS OPEN AT 5:30</p>

  <p class="t sans venue">The Gardens at Coral Point</p>
  <p class="t sans address">81500 SEAVIEW HIGHWAY ISLAMORADA</p>
  <p class="t sans address-sub">(MM81 BAYSIDE BEHIND HARBOR MARKET)</p>

  <p class="t sans tickets">TICKETS $15 each<span class="sep">|</span>Drinks included</p>
  <p class="t sans guest">NAMES MUST BE ON THE GUEST LIST</p>

  <p class="t serif signoff">Hope to see you there!</p>

  <div class="contact-band"></div>
  <p class="contact contact-title">CONTACT MARISOL VANCE FOR TICKETS:</p>
  <p class="contact contact-line">hello@brightpathlifecoach.com<span class="sep">|</span>305-555-0147</p>
</div>
</body>
</html>
```